Property Auctions with Gareth Whitlow

Podcast cover art 3000px by 3000px. Eye catching for a weekly podcast. The words should read Property Auctions (large font) with Gareth Whitlow (smaller font)

I would like the font and colours to be similar to my book, a copy of which I have attached.

Target Market(s)

New and experienced property investors looking to purchase at a property auction

```html
<!DOCTYPE html>
<html lang="en">
<head>
<meta charset="utf-8">
<title>Property Auctions with Gareth Whitlow — Podcast Cover</title>
<link href="https://fonts.googleapis.com/css2?family=Archivo:wdth,wght@75,800&family=Barlow+Semi+Condensed:wght@500&display=swap" rel="stylesheet">
<style>
  :root {
    --slate: #283236;
    --slate-soft: #3a4644;
    --photo-mid: #56605a;
    --gold: #e1b55a;
    --gold-deep: #c8953a;
    --gold-light: #f6d98a;
    --cream: #f3e4c0;
    --white: #ffffff;
    --green: #6bb83c;
  }
  html, body {
    margin: 0;
    padding: 0;
    overflow: hidden;
    background: var(--slate);
  }
  .cover {
    position: relative;
    width: 1200px;
    height: 1200px;
    overflow: hidden;
    background: var(--slate);
  }
  .scene-photo {
    position: absolute;
    left: 0;
    top: 500px;
    width: 1200px;
    height: 700px;
    background:
      radial-gradient(ellipse 420px 260px at 720px 420px, rgba(90,100,92,0.75), transparent 70%),
      radial-gradient(ellipse 240px 200px at 900px 200px, rgba(120,70,70,0.35), transparent 70%),
      linear-gradient(to bottom, var(--slate) 0%, var(--slate-soft) 35%, var(--photo-mid) 100%);
  }
  .title {
    position: absolute;
    left: 0;
    top: 0;
    margin: 0;
    width: 1200px;
    height: 520px;
  }
  .title svg { display: block; }
  .title-line {
    font-family: "Archivo", sans-serif;
    font-stretch: 75%;
    font-variation-settings: "wdth" 75;
    font-weight: 800;
    font-size: 200px;
    fill: var(--gold);
  }
  .host-rule {
    position: absolute;
    left: 0;
    top: 556px;
    width: 452px;
    height: 22px;
    background: var(--gold);
  }
  .host {
    position: absolute;
    left: 486px;
    top: 536px;
    margin: 0;
    font-family: "Barlow Semi Condensed", sans-serif;
    font-weight: 500;
    font-size: 48px;
    line-height: 56px;
    color: var(--white);
    letter-spacing: -0.5px;
    white-space: nowrap;
  }
  .host .name { text-transform: uppercase; }
  .decor {
    position: absolute;
    inset: 0;
  }
</style>
</head>
<body>
<main class="cover">
  <div class="scene-photo" role="img" aria-label="Blurred photo of a small model house and key on stone, with a For Sale sign in the background"></div>

  <h1 class="title" aria-label="Property Auctions">
    <svg width="1200" height="520" viewBox="0 0 1200 520" aria-hidden="true">
      <text class="title-line" x="120" y="264" textLength="792" lengthAdjust="spacingAndGlyphs">PROPERTY</text>
      <text class="title-line" x="115" y="480" textLength="786" lengthAdjust="spacingAndGlyphs">AUCTIONS</text>
    </svg>
  </h1>

  <div class="host-rule"></div>
  <p class="host">with <span class="name">Gareth Whitlow</span></p>

  <svg class="decor" width="1200" height="1200" viewBox="0 0 1200 1200">
    <defs>
      <radialGradient id="coinGold" cx="40%" cy="35%" r="70%">
        <stop offset="0%" stop-color="#f6d98a"/>
        <stop offset="100%" stop-color="#c8953a"/>
      </radialGradient>
      <linearGradient id="symbolGold" x1="0" y1="0" x2="1" y2="1">
        <stop offset="0%" stop-color="#f6d98a"/>
        <stop offset="100%" stop-color="#c8953a"/>
      </linearGradient>
    </defs>

    <g role="img" aria-label="Gold pound coin illustration">
      <ellipse cx="1082" cy="250" rx="110" ry="116" fill="url(#coinGold)"/>
    </g>
    <path class="up-arrow" d="M1104 154 L1102 96 L1090 96 L1142 34 L1196 82 L1174 86 L1162 150 Z" fill="var(--green)"/>

    <g role="img" aria-label="Floating gold pound sign illustrations">
      <rect x="68" y="660" width="64" height="52" rx="20" fill="url(#symbolGold)" opacity="0.85"/>
      <rect x="196" y="704" width="88" height="104" rx="30" fill="url(#symbolGold)"/>
      <rect x="100" y="864" width="156" height="240" rx="50" fill="url(#symbolGold)"/>
    </g>

    <g role="img" aria-label="Two gold pound coins on a slope">
      <circle cx="1064" cy="926" r="116" fill="url(#coinGold)"/>
      <circle cx="936" cy="1010" r="92" fill="url(#coinGold)"/>
    </g>

    <polygon points="16,1200 1200,956 1200,1040 40,1200" fill="var(--cream)"/>
    <polygon points="40,1200 1200,1040 1200,1120 600,1200" fill="var(--gold)"/>
    <polygon points="600,1200 1200,1120 1200,1200" fill="var(--slate)"/>
  </svg>
</main>
</body>
</html>
```